Cardiologist needs a unique and unforgettable business card design

Hi, I am a Cardiologist (heart specialist) and I need a business card as I am starting out my own practice very soon.
I have so used to seeing very boring and forgettable business cards that people take one look and then it goes into the bin.
I hope you can design one card that tells people immediately that it is from a Cardiologist (Heart Specialist) who is good, experienced, mature and save lives.
My colours that I like are green/white/earthly tones but I am also open to various colours combinations.
My clinic name is called Veyla Cardiology and I am attaching the Logo and information needed on the name card for you.
I would like the definition of Veyla to be in the name card
Veyla - To save one suffering from disease, to make well, heal, preserve,
restore to health and to make whole one again
I would like to have Spot UV or Embossing or Both to make the card stand out.
Thank you very much
Clinic

```html
<!DOCTYPE html>
<html lang="en">
<head>
<meta charset="utf-8">
<title>Veyla Cardiology – Business Card</title>
<link rel="stylesheet" href="https://fonts.googleapis.com/css2?family=Arimo:wght@400;700&family=Exo+2:wght@700&family=Noto+Sans+SC:wght@400&display=swap">
<style>
  :root {
    --bg: #1e1e1e;
    --paper: #f7f7f7;
    --ink: #2b2b2b;
    --ink-soft: #444444;
    --red: #b3141b;
    --red-deep: #8f0d12;
    --on-red: #ffffff;
    --on-red-soft: #f3d6d7;
  }
  * { margin: 0; padding: 0; box-sizing: border-box; }
  html, body {
    width: 1200px; height: 873px; overflow: hidden;
    background: var(--bg);
    font-family: "Arimo", Arial, sans-serif;
    color: var(--ink);
  }
  .stage {
    position: relative; width: 1200px; height: 873px;
  }
  .card {
    position: absolute;
    width: 540px; height: 310px;
    background: var(--paper);
    box-shadow: 0 10px 30px rgba(0,0,0,.55);
    overflow: hidden;
  }
  .card--front { left: 40px; top: 170px; }
  .card--back  { left: 620px; top: 393px; }

  /* brand name set as plain text */
  .brand {
    position: absolute;
    display: flex; align-items: center; gap: 10px;
    font-size: 27px; font-weight: 400; letter-spacing: 2px;
    color: var(--ink);
    text-transform: uppercase;
  }
  .brand__dot {
    width: 14px; height: 14px; border-radius: 50%;
    background: var(--red);
  }

  /* front */
  .card--front .brand { left: 30px; top: 128px; }
  .doctor {
    position: absolute; right: 30px; top: 24px; text-align: right;
  }
  .doctor__chinese-name { font-family: "Noto Sans SC", sans-serif; font-size: 11px; color: var(--ink-soft); }
  .doctor__name { font-size: 14px; font-weight: 700; color: var(--red); margin-top: 2px; }
  .doctor__title { font-size: 9.5px; color: var(--ink-soft); margin-top: 3px; }
  .doctor__title-cn { font-family: "Noto Sans SC", sans-serif; font-size: 11px; color: var(--ink); margin-top: 2px; }
  .credentials {
    position: absolute; right: 30px; top: 112px; text-align: right;
    font-size: 11px; line-height: 1.5; color: var(--ink-soft); list-style: none;
  }
  .credentials li:nth-child(3) { margin-bottom: 14px; }

  .contacts { position: absolute; list-style: none; }
  .contacts li { display: flex; align-items: center; gap: 10px; font-size: 12px; line-height: 1; margin-bottom: 11px; }
  .contacts svg { width: 13px; height: 13px; flex: none; }
  .card--front .contacts { left: 30px; bottom: 14px; color: var(--ink-soft); }
  .card--front .contacts svg { color: var(--red); }

  /* back */
  .card--back .panel {
    position: absolute; left: 0; right: 0; bottom: 0; height: 176px;
    background: linear-gradient(180deg, var(--red) 0%, var(--red-deep) 100%);
  }
  .card--back .brand { left: 30px; top: 58px; }
  .definition {
    position: absolute; right: 28px; top: 20px; text-align: right;
    font-size: 12.5px; line-height: 1.45; color: var(--ink);
  }
  .definition__sign {
    font-family: "Exo 2", sans-serif; font-weight: 700; color: var(--red); font-size: 13px;
  }
  .clinic { position: absolute; left: 70px; top: 148px; color: var(--on-red); }
  .clinic__name { font-family: "Exo 2", sans-serif; font-weight: 700; font-size: 13.5px; letter-spacing: .5px; }
  .clinic__address { font-size: 10.5px; color: var(--on-red-soft); margin-top: 2px; }
  .hours {
    position: absolute; right: 24px; top: 182px; text-align: right;
    font-size: 10.5px; line-height: 1.55; color: var(--on-red-soft); list-style: none;
  }
  .hours li.gap { margin-top: 6px; }
  .card--back .contacts { left: 30px; bottom: 8px; color: var(--on-red); }
  .card--back .contacts li { font-size: 12.5px; margin-bottom: 13px; }
</style>
</head>
<body>
<main class="stage">

  <!-- front of card -->
  <section class="card card--front" aria-label="Business card front">
    <div class="brand"><span class="brand__dot"></span>Veyla Cardiology</div>

    <div class="doctor">
      <p class="doctor__chinese-name">(林凯文医生)</p>
      <p class="doctor__name">DR LIM KAI WEN</p>
      <p class="doctor__title">Consultant General &amp; Interventional Cardiologist</p>
      <p class="doctor__title-cn">心脏及介入性心脏专科医生</p>
    </div>

    <ul class="credentials">
      <li>MBBS(S'pore)</li>
      <li>MRCP (United Kingdom)</li>
      <li>FRCP (Edinburgh)</li>
      <li>FACC (USA), FAMS (Cardiology)</li>
      <li>ACSM (Clinical Exercise Physiologist; USA)</li>
    </ul>

    <ul class="contacts">
      <li>
        <svg viewBox="0 0 14 14" aria-hidden="true"><rect x="3" y="1" width="8" height="12" rx="1.5" fill="none" stroke="currentColor" stroke-width="1.4"/></svg>
        555-014-3827
      </li>
      <li>
        <svg viewBox="0 0 14 14" aria-hidden="true"><path d="M6 8l2-2M5 6L3 8a2 2 0 0 0 3 3l2-2M9 8l2-2a2 2 0 0 0-3-3L6 5" fill="none" stroke="currentColor" stroke-width="1.4" stroke-linecap="round"/></svg>
        www.veylacardiology.com
      </li>
      <li>
        <svg viewBox="0 0 14 14" aria-hidden="true"><rect x="1" y="3" width="12" height="8" fill="currentColor"/><path d="M1 3l6 5 6-5" fill="none" stroke="var(--paper)" stroke-width="1.1"/></svg>
        drlimkaiwen@veylacardiology.com
      </li>
    </ul>
  </section>

  <!-- back of card -->
  <section class="card card--back" aria-label="Business card back">
    <div class="panel"></div>

    <div class="brand"><span class="brand__dot"></span>Veyla Cardiology</div>

    <p class="definition">
      To save one suffering from disease<br>
      to make well, heal, preserve<br>
      restore to health and to<br>
      make whole one again<br>
      <span class="definition__sign">...VEYLA</span>
    </p>

    <div class="clinic">
      <p class="clinic__name">HARBOURVIEW SPECIALIST CENTRE</p>
      <p class="clinic__address">12 Meranti Road, #04-17, Singapore 308412</p>
    </div>

    <ul class="hours">
      <li>Monday to Friday : 9:00 am to 1:00 pm</li>
      <li>2:00 pm to 5:00 pm</li>
      <li class="gap">Saturday : 9:00 am to 1:00 pm</li>
      <li>Sunday and Public Holidays: Closed</li>
    </ul>

    <ul class="contacts">
      <li>
        <svg viewBox="0 0 14 14" aria-hidden="true"><rect x="3" y="1" width="8" height="12" rx="1.5" fill="none" stroke="currentColor" stroke-width="1.4"/></svg>
        555-014-3827
      </li>
      <li>
        <svg viewBox="0 0 14 14" aria-hidden="true"><path d="M6 8l2-2M5 6L3 8a2 2 0 0 0 3 3l2-2M9 8l2-2a2 2 0 0 0-3-3L6 5" fill="none" stroke="currentColor" stroke-width="1.4" stroke-linecap="round"/></svg>
        www.veylacardiology.com
      </li>
      <li>
        <svg viewBox="0 0 14 14" aria-hidden="true"><rect x="1" y="3" width="12" height="8" fill="currentColor"/><path d="M1 3l6 5 6-5" fill="none" stroke="var(--red)" stroke-width="1.1"/></svg>
        drlimkaiwen@veylacardiology.com
      </li>
    </ul>
  </section>

</main>
</body>
</html>
```